Vintage home page design (Bellweather Coupes and Wagons - 7815)

Wants a vintage-themed website.
http://www.bellweathercoupeshub.com/
Likes the retro graphics used on this site (the signs and the cartoon at the bottom of the boy holding the flag)

Client is open to a light or dark background, and wants to see what you come up with. Use their logo colors as accent colors throughout the home page design.
Keep it retro and vintage and have fun!

Attached their logo and a .psd layout example. The layout example is just for referencing the dimensions we usually use, but it's not set in stone.

Let me know if you have any questions and I'll answer them as soon as possible.

Thank you designers for your early submissions! I am waiting to hear back from the client and will keep each of you updated when they reply. Best regards, Maribel

Hello everyone- Thanks so much for being patient, I am still waiting to hear back from the client and get feedback. I just sent another follow up email and will let you all know when I get feedback. Best regards, Maribel

```html
<!DOCTYPE html>
<html lang="en">
<head>
<meta charset="utf-8">
<title>Bellweather Coupes and Wagons</title>
<link rel="stylesheet" href="https://fonts.googleapis.com/css2?family=Oswald:wght@500;700&family=Roboto+Condensed:wght@400&family=Montserrat:wght@400&family=Open+Sans:wght@600;700&family=Alfa+Slab+One&display=swap">
<style>
:root{
  --red:#c8101e;
  --red-dark:#9b0a10;
  --red-fold:#6e070b;
  --navy:#283580;
  --cream:#ecdfb8;
  --paper:#f3efe6;
  --stripe-bg:#e6cf9f;
  --slate:#4c6a80;
  --panel:#e2d4ae;
  --tan:#b8843f;
  --text-red:#d0141f;
  --white:#ffffff;
}
*{box-sizing:border-box;margin:0;padding:0}
html,body{width:1077px;height:1200px;overflow:hidden}
body{position:relative;background:var(--cream);font-family:"Montserrat",sans-serif}
.abs{position:absolute}

.top-backdrop{left:0;top:0;width:1077px;height:370px;background:linear-gradient(135deg,#eed8a8,#dcbd86 50%,#e9d2a2)}
.top-edge{left:0;top:0;width:1077px;height:12px;background:var(--red-dark)}
.backdrop-rule{left:0;top:368px;width:1077px;height:5px;background:var(--navy)}

.paper-band{left:122px;top:106px;width:833px;height:93px;background:var(--paper)}
.nav-ribbon-end{top:120px;width:70px;height:50px;background:#e01d2b}
.nav-ribbon-end.left{left:61px;clip-path:polygon(0 0,100% 0,100% 100%,0 100%,18% 50%)}
.nav-ribbon-end.right{left:941px;clip-path:polygon(0 0,100% 0,82% 50%,100% 100%,0 100%)}
.nav-bar{left:116px;top:128px;width:845px;height:49px;background:linear-gradient(#e2202d,var(--red));box-shadow:0 2px 3px rgba(0,0,0,.3)}
.main-nav{left:393px;top:128px;height:49px;display:flex;align-items:center;gap:0}
.main-nav a{font-family:"Roboto Condensed",sans-serif;font-size:17px;color:var(--white);text-decoration:none;margin-right:30px}

.brand{left:140px;top:22px;width:150px;height:150px;background:var(--navy);display:flex;align-items:center;justify-content:center;text-align:center;padding:10px}
.brand span{font-family:"Oswald",sans-serif;font-weight:500;font-size:19px;line-height:1.15;color:var(--white)}

.phone{left:706px;top:60px;display:flex;align-items:center;gap:6px}
.phone span{font-family:"Oswald",sans-serif;font-weight:700;font-size:27px;color:var(--red)}

.hero{left:122px;top:199px;width:833px;height:282px;background:linear-gradient(#b9cde0 0%,#d9e2e8 22%,#8a7a50 32%,#c2642a 60%,#b04a18 100%)}
.slider-dots{left:504px;top:459px;display:flex;gap:6px}
.slider-dots i{display:block;width:13px;height:13px;background:var(--white);border:1px solid #ccc}
.slider-dots i.on{background:#8a2a2a}

.tab-band{left:103px;top:483px;width:872px;height:67px;background:var(--red-dark)}
.tab-fold{top:550px;width:20px;height:22px;background:var(--red-fold)}
.tab-fold.left{left:103px;clip-path:polygon(0 0,100% 0,100% 100%)}
.tab-fold.right{left:955px;clip-path:polygon(0 0,100% 0,0 100%)}
.tabs{left:149px;top:503px;display:flex;gap:53px}
.tabs a{font-family:"Roboto Condensed",sans-serif;font-size:22px;color:var(--white);text-decoration:none}

.vip{left:712px;top:495px;width:179px;height:107px;background:var(--slate);border:2px solid #8fa7b8;border-radius:14px;text-align:center;box-shadow:0 2px 3px rgba(0,0,0,.3)}
.vip .join{font-family:"Oswald",sans-serif;font-weight:500;font-size:23px;color:var(--white);margin-top:14px;letter-spacing:1px}
.vip .list{font-family:"Alfa Slab One",serif;font-size:27px;color:var(--white);line-height:1}

.welcome{left:124px;top:573px;width:248px}
.welcome h1{font-family:"Alfa Slab One",serif;font-size:46px;font-weight:400;color:var(--red);line-height:1}
.welcome .band{margin-top:6px;background:var(--navy);padding:10px 10px;font-family:"Montserrat",sans-serif;font-size:13px;color:var(--white);text-align:center}

.copy{font-size:12.2px;line-height:16.3px;color:var(--text-red)}
.copy.one{left:385px;top:634px;width:310px}
.copy.two{left:136px;top:717px;width:562px}

.contact{left:731px;top:610px;width:223px;height:199px;background:var(--panel)}
.contact-head{left:731px;top:610px;width:223px;height:57px;background:linear-gradient(#9a2a22,#7d1d18);border-top:6px solid #23383f;border-bottom:5px solid #23383f}
.contact-head h2{font-family:"Open Sans",sans-serif;font-weight:700;font-size:24px;color:var(--white);position:absolute;right:12px;top:8px}
.contact-list{left:750px;top:674px;width:200px;list-style:none}
.contact-list li{display:flex;gap:7px;font-size:12px;line-height:16.3px;color:var(--text-red);margin-bottom:7px}
.contact-list svg{flex:none;margin-top:1px}

.featured{left:122px;top:842px;width:833px;height:187px;background:linear-gradient(#c4914b,var(--tan) 50%,#a97432);border-radius:3px}
.featured h2{position:absolute;left:31px;top:10px;font-family:"Open Sans",sans-serif;font-weight:700;font-size:29px;color:var(--white);text-shadow:1px 2px 2px rgba(0,0,0,.5)}
.thumb{top:902px;width:184px;height:100px;border:2px solid var(--white)}
.t1{left:155px;background:linear-gradient(#e4e4e4,#9aa8a0)}
.t2{left:349px;background:linear-gradient(#7a5060,#9a3a30)}
.t3{left:543px;background:linear-gradient(#ffffff,#e84040 60%,#f2f2f2)}
.t4{left:737px;background:linear-gradient(#8a3a58,#b9dbe8 60%,#d8d0d0)}
.arrow{top:934px}
.arrow.left{left:126px}
.arrow.right{left:927px}

.footer{left:0;top:1040px;width:1077px;height:160px;background:var(--navy)}
.footer-links{left:142px;top:1074px;font-family:"Open Sans",sans-serif;font-weight:600;font-size:12px;color:var(--white)}
.footer-links a{color:var(--white);text-decoration:none}
.copyright{left:141px;top:1110px;font-family:"Open Sans",sans-serif;font-weight:600;font-size:10px;color:var(--white)}
.quality-badge{left:691px;top:1045px;width:171px;height:143px;background:linear-gradient(#3a5a8a,#b9dbe6);border-radius:6px;opacity:.9}
</style>
</head>
<body>
<div class="abs top-backdrop" role="img" aria-label="Diagonal retro stripes in tan, orange and brown"></div>
<div class="abs top-edge"></div>
<div class="abs backdrop-rule"></div>

<div class="abs paper-band"></div>
<div class="abs nav-ribbon-end left"></div>
<div class="abs nav-ribbon-end right"></div>
<div class="abs nav-bar"></div>
<nav class="abs main-nav">
  <a href="#">Home</a><a href="#">Inventory</a><a href="#">About Us</a><a href="#">Sell Your Classic</a><a href="#">Contact Us</a><a href="#">VIP List</a>
</nav>

<div class="abs brand"><span>Bellweather Coupes and Wagons</span></div>

<div class="abs phone">
  <svg width="34" height="34" viewBox="0 0 24 24"><path fill="#222" d="M6.6 10.8a15.1 15.1 0 0 0 6.6 6.6l2.2-2.2c.3-.3.7-.4 1-.2 1.1.4 2.3.6 3.6.6.6 0 1 .4 1 1V20c0 .6-.4 1-1 1A17 17 0 0 1 3 4c0-.6.4-1 1-1h3.5c.6 0 1 .4 1 1 0 1.3.2 2.5.6 3.6.1.3 0 .7-.2 1z"/></svg>
  <span>(209) XXXX XXXX</span>
</div>

<div class="abs hero" role="img" aria-label="Photo of a turquoise and white 1950s hardtop in a red desert landscape"></div>
<div class="abs slider-dots"><i class="on"></i><i></i><i></i><i></i></div>

<div class="abs tab-band"></div>
<div class="abs tab-fold left"></div>
<div class="abs tab-fold right"></div>
<nav class="abs tabs"><a href="#">VIEW INVENTORY</a><a href="#">RECENT SALES</a></nav>

<a class="abs vip" href="#"><div class="join">Join our</div><div class="list">VIP LIST</div></a>

<div class="abs welcome">
  <h1>Welcome</h1>
  <div class="band">Bellweather Coupes and Wagons</div>
</div>

<p class="abs copy one">Lorem Ipsum. Proin gravida nibh vel velit auctor aliquet. Aenean sollicitudin, lorem quis bibendum auctor, nisi elit consequat ipsum, nec sagittis sem nibh id elit. Duis sed odio sit amet nibh vulputate cursus a sit amet mauris. Morbi accumsan ipsum</p>
<p class="abs copy two">Lorem Ipsum. Proin gravida nibh vel velit auctor aliquet. Aenean sollicitudin, lorem quis bibendum auctor, nisi elit consequat ipsum, nec sagittis sem nibh id elit. Duis sed odio sit amet nibh vulputate cursus a sit amet mauris. Morbi accumsan ipsum velit. Nam nec tellus a odio tincidunt auctor a ornare odio. Sed non &nbsp;mauris vitae erat consequat auctor eu in elit. Class aptent taciti sociosqu ad litora torquent per conubia nostra, per inceptos</p>

<div class="abs contact"></div>
<div class="abs contact-head"><h2>Contact info</h2></div>
<ul class="abs contact-list">
  <li><svg width="14" height="18" viewBox="0 0 14 18"><path fill="#222" d="M7 0a7 7 0 0 0-7 7c0 5 7 11 7 11s7-6 7-11a7 7 0 0 0-7-7zm0 10a3 3 0 1 1 0-6 3 3 0 0 1 0 6z"/></svg><span>Lorem Ipsum. Proin gravida nibh vel velit auctor aliquet. Aenean sollicitudin, lorem</span></li>
  <li><svg width="13" height="12" viewBox="0 0 13 12"><path fill="#222" d="M0 3c0-2 3-3 6.5-3S13 1 13 3v1H9V3H4v1H0zM2 5h9l1 7H1z"/></svg><span>(209) XXXX XXXX</span></li>
  <li><svg width="13" height="12" viewBox="0 0 13 12"><path fill="#222" d="M3 0h7v3H3zM0 4h13v6h-2V8H2v2H0zM3 9h7v3H3z"/></svg><span>(209) XXXX XXXX</span></li>
  <li><svg width="13" height="12" viewBox="0 0 13 12"><path fill="#222" d="M0 5l6.5-5L13 5v7H0zm1.5 1v4.5h10V6l-5 3z"/></svg><span>info@domainname.com</span></li>
</ul>

<section class="abs featured"><h2>Featured Vehicles</h2></section>
<div class="abs thumb t1" role="img" aria-label="Photo of a green vintage touring car"></div>
<div class="abs thumb t2" role="img" aria-label="Photo of a red vintage sedan"></div>
<div class="abs thumb t3" role="img" aria-label="Photo of a red late-1950s convertible"></div>
<div class="abs thumb t4" role="img" aria-label="Photo of a light blue and white 1950s coupe"></div>
<svg class="abs arrow left" width="24" height="36" viewBox="0 0 24 36"><path d="M20 2L4 18l16 16" fill="none" stroke="#283580" stroke-width="4"/></svg>
<svg class="abs arrow right" width="24" height="36" viewBox="0 0 24 36"><path d="M4 2l16 16L4 34" fill="none" stroke="#283580" stroke-width="4"/></svg>

<footer class="abs footer"></footer>
<div class="abs footer-links"><a href="#">Home</a> &nbsp;| &nbsp;&nbsp;<a href="#">Inventory</a> &nbsp;| &nbsp;&nbsp;<a href="#">Site Map</a> &nbsp;| &nbsp;&nbsp;<a href="#">Contact Us</a></div>
<div class="abs copyright">Copyright © 2003-2014 Gearline Media, LTD. All Rights Reserved.</div>
<div class="abs quality-badge" role="img" aria-label="Illustration of a biplane towing a Quality Guaranteed banner"></div>
</body>
</html>
```